simple, clean, smart design for PPT template!

We need a template design for ouw company Brenthollow. Please refer to the business cad design and our web site.

Our message is Wisdome and Knowledge, and the image is "simple" and "clean".
http://www.brenthollow.example/

You may want to refer to the company like KDT, Solvarine, RMN, Tyvor, etc.

Target Market(s)

Every business industry.

Industry/Entity Type

Consulting

Font styles to use
Other font styles liked:
• Please refer to your sense from our corporate image.

Requirements
Must have
• company logo. the colors should be limited to ones used for the logo. The final version of your file must be submitted in PPT format.
Nice to have
• The corporate image is always "simple and clean".
Should not have
• No pictures of human face.

```html
<!DOCTYPE html>
<html lang="en">
<head>
<meta charset="utf-8">
<title>Brenthollow PowerPoint Template Design_01</title>
<link href="https://fonts.googleapis.com/css2?family=Questrial&family=Montserrat:wght@600;700&display=swap" rel="stylesheet">
<style>
  :root{
    --green:#9ccb52;
    --green-light:#c6e19b;
    --grey-bar:#b9b9c2;
    --ink:#222;
    --text:#3a3a3a;
    --muted:#8a8a8a;
    --rule:#9a9a9a;
    --page:#ffffff;
  }
  *{box-sizing:border-box;margin:0;padding:0}
  html,body{width:1200px;height:1000px;overflow:hidden;background:var(--page)}
  body{position:relative;font-family:"Questrial",sans-serif;color:var(--text)}
  .sheet-title{position:absolute;top:55px;left:0;width:1200px;text-align:center;font-size:15px;font-weight:400;color:var(--ink)}
  .caption{position:absolute;font-size:14px;color:var(--ink);transform:translateX(-50%);white-space:nowrap}
  .slide{position:absolute;width:353px;height:198px;background:#fff;overflow:hidden;
    box-shadow:2px 3px 5px rgba(0,0,0,.35);border:1px solid #e4e4e4}
  .heading{position:absolute;left:15px;top:14px;font-size:14px;color:var(--green)}
  .heading::after{content:"";position:absolute;left:0;top:21px;width:42px;height:1px;background:var(--green)}
  .lead{position:absolute;left:15px;top:49px;font-family:"Montserrat",sans-serif;font-weight:700;font-size:7px;color:var(--ink)}
  .body{position:absolute;left:15px;width:318px;font-size:7.9px;line-height:1.24;color:var(--text)}
  .body p+p{margin-top:8px}
  .footer{position:absolute;left:0;right:0;bottom:0;height:22px;border-top:1px solid var(--rule)}
  .footer span{position:absolute;top:8px;font-size:4.6px;letter-spacing:.2px;color:var(--green)}
  .footer .brand{left:15px}
  .footer .page{right:13px;color:var(--muted)}
  .cover .topbar{position:absolute;left:0;top:0;width:100%;height:33px;background:#fff}
  .logo{position:absolute;left:15px;top:9px;display:flex;align-items:center;gap:4px;font-size:13px;color:var(--green)}
  .logo i{display:block;width:13px;height:13px;border-radius:50%;background:var(--green)}
  .cover .field{position:absolute;left:0;top:33px;width:100%;height:165px;background:var(--green)}
  .cover-title{position:absolute;left:15px;top:51px;font-size:15px;color:#fff}
  .white-rule{position:absolute;left:15px;width:42px;height:1px;background:#fff}
  .cover-sub{position:absolute;left:15px;top:150px;font-family:"Montserrat",sans-serif;font-weight:700;font-size:7.5px;color:#fff}
  .cover-by{position:absolute;left:15px;top:166px;font-size:8.3px;color:#fff}
  .cover-date{position:absolute;left:15px;top:180px;font-size:6px;color:#fff}
  .photo{position:absolute}
  .photo-office{left:0;top:113px;width:353px;height:85px;
    background:linear-gradient(180deg,#b9bcc4 0%,#7d8089 45%,#2c2f38 100%)}
  .photo-desk{left:213px;top:0;width:140px;height:198px;
    background:linear-gradient(160deg,#6d717a 0%,#4a4d55 45%,#2b2d33 100%)}
  .question{position:absolute;left:15px;top:72px;width:180px;font-family:"Montserrat",sans-serif;font-weight:600;font-size:10.5px;line-height:1.3;color:var(--ink)}
  .question-note{position:absolute;left:15px;top:111px;width:160px;font-size:6.6px;line-height:1.3}
  .tomb{position:absolute;width:98px;border-top:3px solid var(--green);padding-top:5px}
  .tomb h4{font-family:"Montserrat",sans-serif;font-weight:700;font-size:6.2px;color:var(--ink);margin-bottom:4px}
  .tomb p{font-size:5.8px;line-height:1.25;width:88px}
  .tomb p+p{margin-top:3px}
  .member{position:absolute;top:43px;width:98px}
  .member .portrait{width:98px;height:50px;background:linear-gradient(180deg,#e2e2e2,#b5b5b5)}
  .member .bar{height:3px;background:var(--green);margin-top:3px}
  .member h4{font-family:"Montserrat",sans-serif;font-weight:700;font-size:6.5px;color:var(--ink);margin-top:7px}
  .member p{font-size:5.3px;line-height:1.45}
  .member .role{font-size:5.8px;margin-bottom:2px}
  .section{background:var(--green);border-color:var(--green)}
  .thanks{position:absolute;left:15px;top:146px;font-size:15px;color:#fff}
  .chart{position:absolute;left:0;top:0}
</style>
</head>
<body>
  <h1 class="sheet-title">Brenthollow LLC Powerpoint Template Design_01</h1>

  <section class="slide cover" style="left:48px;top:95px">
    <div class="topbar"></div>
    <div class="logo"><i></i>brenthollow</div>
    <div class="field"></div>
    <div class="cover-title">Presentation Title</div>
    <div class="white-rule" style="top:142px"></div>
    <div class="cover-sub">Presentation Subtitle</div>
    <div class="cover-by">Presented by Kenta Morikawa, Founder &amp; CEO</div>
    <div class="cover-date">April 2016</div>
  </section>

  <section class="slide" style="left:424px;top:95px">
    <div class="heading">About Brenthollow</div>
    <div class="body" style="top:49px">A group of over 80 professionals works to provide you with outstanding back office services you can trust. Our members include experts from leading consulting firms, all with over ten years of experience in the back office functions of multinationals in Japan, and many are nationally certified, bilingual specialists.</div>
    <div class="photo photo-office" role="img" aria-label="Silhouettes of a business team meeting in front of a bright office window"></div>
  </section>

  <section class="slide" style="left:800px;top:95px">
    <div class="heading">What we do</div>
    <div class="lead">We are your remote local back office.</div>
    <div class="body" style="top:68px">
      <p>From starting up your business in Japan to the back office services that keep it running, we provide the bilingual support you need for every phase of your business. We'll meet the needs of your business with an expert team of professionals with national certifications and multinational experience in every back office area. Rather than outsourcing to independent specialists, you'll receive day-to-day support as we work together with you as your remote back office "division."</p>
      <p>We handle not only finance, human resources, legal and IT back office services, but we also provide a concierge service to help you take care of the details of daily operation in Japan quickly and accurately.</p>
    </div>
    <div class="footer"><span class="brand">BRENTHOLLOW LLC &nbsp;|&nbsp; CLARITY &amp; EXPERTISE</span><span class="page">2</span></div>
  </section>

  <div class="caption" style="left:224px;top:314px">Front Cover Slide</div>
  <div class="caption" style="left:788px;top:314px">Interior Slides</div>

  <section class="slide" style="left:48px;top:389px">
    <div class="heading">What we do</div>
    <div class="lead">We are your remote local back office.</div>
    <div class="body" style="top:68px">
      <p>From starting up your business in Japan to the back office services that keep it running, we provide the bilingual support you need for every phase of your business. We'll meet the needs of your business with an expert team of professionals with national certifications and multinational experience in every back office area. Rather than outsourcing to independent specialists, you'll receive day-to-day support as we work together with you as your remote back office "division."</p>
      <p>We handle not only finance, human resources, legal and IT back office services, but we also provide a concierge service to help you take care of the details of daily operation in Japan quickly and accurately.</p>
    </div>
    <div class="footer"><span class="brand">BRENTHOLLOW LLC &nbsp;|&nbsp; CLARITY &amp; EXPERTISE</span><span class="page">2</span></div>
  </section>

  <section class="slide" style="left:424px;top:389px">
    <div class="question">Are you looking for a remote back office solution in Japan?</div>
    <div class="question-note">Let Brenthollow take care of all your requirements, from establishing a company in Japan to back office operations.</div>
    <div class="photo photo-desk" role="img" aria-label="Hands holding a coffee cup beside a laptop keyboard"></div>
  </section>

  <section class="slide" style="left:800px;top:389px">
    <div class="heading">Tombstone slide</div>
    <div class="tomb" style="left:15px;top:48px"><h4>Client Name</h4><p>Lorem ipsum dolor sit amet consectetur adipiscing elit</p><p>Vestibulum consectetur sed ipsum nec imperdiet</p></div>
    <div class="tomb" style="left:127px;top:48px"><h4>Client Name</h4><p>Lorem ipsum dolor sit amet consectetur adipiscing elit</p><p>Vestibulum consectetur sed ipsum nec imperdiet</p></div>
    <div class="tomb" style="left:240px;top:48px"><h4>Client Name</h4><p>Lorem ipsum dolor sit amet consectetur adipiscing elit</p><p>Vestibulum consectetur sed ipsum nec imperdiet</p></div>
    <div class="tomb" style="left:15px;top:112px"><h4>Client Name</h4><p>Lorem ipsum dolor sit amet consectetur adipiscing elit</p><p>Vestibulum consectetur sed ipsum nec imperdiet</p></div>
    <div class="tomb" style="left:127px;top:112px"><h4>Client Name</h4><p>Lorem ipsum dolor sit amet consectetur adipiscing elit</p><p>Vestibulum consectetur sed ipsum nec imperdiet</p></div>
    <div class="tomb" style="left:240px;top:112px"><h4>Client Name</h4><p>Lorem ipsum dolor sit amet consectetur adipiscing elit</p><p>Vestibulum consectetur sed ipsum nec imperdiet</p></div>
    <div class="footer"><span class="brand">BRENTHOLLOW LLC &nbsp;|&nbsp; CLARITY &amp; EXPERTISE</span><span class="page">5</span></div>
  </section>

  <div class="caption" style="left:600px;top:608px">Interior Slides</div>

  <section class="slide" style="left:48px;top:683px">
    <div class="heading">Our team</div>
    <div class="member" style="left:15px">
      <div class="portrait" role="img" aria-label="Portrait photo of team member"></div><div class="bar"></div>
      <h4>Kenta Morikawa</h4><p class="role">Founder &amp; CEO</p>
      <p>T +81 (0) 3 5550 0142</p><p>E k.morikawa@brenthollow.example</p>
    </div>
    <div class="member" style="left:127px">
      <div class="portrait" role="img" aria-label="Portrait photo of team member"></div><div class="bar"></div>
      <h4>Aya Sunohara</h4><p class="role">Partner, Tokyo</p>
      <p>T +81 (0) 3 5550 0142</p><p>E a.sunohara@brenthollow.example</p>
    </div>
    <div class="member" style="left:240px">
      <div class="portrait" role="img" aria-label="Portrait photo of team member"></div><div class="bar"></div>
      <h4>Ryo Takemine</h4><p class="role">Legal Counsel</p>
      <p>T +81 (0) 3 5550 0142</p><p>E r.takemine@brenthollow.example</p>
    </div>
    <div class="footer"><span class="brand">BRENTHOLLOW LLC &nbsp;|&nbsp; CLARITY &amp; EXPERTISE</span><span class="page">6</span></div>
  </section>

  <section class="slide" style="left:424px;top:683px">
    <div class="heading">Bar chart</div>
    <svg class="chart" width="353" height="198" viewBox="0 0 353 198" font-family="Questrial, sans-serif">
      <g font-size="5" fill="#333" text-anchor="end">
        <text x="28" y="57">100</text><text x="28" y="66">90</text><text x="28" y="75">80</text>
        <text x="28" y="84">70</text><text x="28" y="93">60</text><text x="28" y="102">50</text>
        <text x="28" y="111">40</text><text x="28" y="120">30</text><text x="28" y="129">20</text>
        <text x="28" y="138">10</text><text x="28" y="147">0</text>
      </g>
      <line x1="32" y1="145" x2="330" y2="145" stroke="#bbb" stroke-width=".6"/>
      <g>
        <rect x="37" y="109" width="8" height="36" fill="var(--green-light)"/>
        <rect x="47" y="120" width="8" height="25" fill="var(--grey-bar)"/>
        <rect x="57" y="64" width="8" height="81" fill="var(--green)"/>
        <rect x="67" y="127" width="8" height="18" fill="var(--grey-bar)"/>
        <rect x="77" y="127" width="8" height="18" fill="var(--green-light)"/>

        <rect x="97" y="116" width="8" height="29" fill="var(--green-light)"/>
        <rect x="107" y="111" width="8" height="34" fill="var(--grey-bar)"/>
        <rect x="117" y="113" width="8" height="32" fill="var(--green)"/>
        <rect x="127" y="116" width="8" height="29" fill="var(--grey-bar)"/>
        <rect x="137" y="134" width="8" height="11" fill="var(--green-light)"/>

        <rect x="157" y="104" width="8" height="41" fill="var(--green-light)"/>
        <rect x="167" y="103" width="8" height="42" fill="var(--grey-bar)"/>
        <rect x="177" y="104" width="8" height="41" fill="var(--green)"/>
        <rect x="187" y="105" width="8" height="40" fill="var(--grey-bar)"/>
        <rect x="197" y="101" width="8" height="44" fill="var(--green-light)"/>

        <rect x="217" y="109" width="8" height="36" fill="var(--green-light)"/>
        <rect x="227" y="111" width="8" height="34" fill="var(--grey-bar)"/>
        <rect x="237" y="113" width="8" height="32" fill="var(--green)"/>
        <rect x="247" y="116" width="8" height="29" fill="var(--grey-bar)"/>
        <rect x="257" y="134" width="8" height="11" fill="var(--green-light)"/>

        <rect x="277" y="117" width="8" height="28" fill="var(--green-light)"/>
        <rect x="287" y="104" width="8" height="41" fill="var(--grey-bar)"/>
        <rect x="297" y="104" width="8" height="41" fill="var(--green)"/>
        <rect x="307" y="105" width="8" height="40" fill="var(--grey-bar)"/>
        <rect x="317" y="101" width="8" height="44" fill="var(--green-light)"/>
      </g>
      <g font-size="5" fill="#333" text-anchor="middle" font-weight="700">
        <text x="61" y="153">1st Qtr</text><text x="121" y="153">2nd Qtr</text>
        <text x="181" y="153">3rd Qtr</text><text x="241" y="153">4th Qtr</text>
        <text x="301" y="153">1st Qtr</text>
      </g>
      <g font-size="4.6" fill="#333">
        <rect x="125" y="159" width="3" height="3" fill="var(--green-light)"/><text x="130" y="162">East</text>
        <rect x="142" y="159" width="3" height="3" fill="var(--grey-bar)"/><text x="147" y="162">West</text>
        <rect x="160" y="159" width="3" height="3" fill="var(--green)"/><text x="165" y="162">North</text>
        <rect x="180" y="159" width="3" height="3" fill="var(--grey-bar)"/><text x="185" y="162">South</text>
        <rect x="200" y="159" width="3" height="3" fill="var(--green-light)"/><text x="205" y="162">Northeast</text>
      </g>
    </svg>
    <div class="footer"><span class="brand">BRENTHOLLOW LLC &nbsp;|&nbsp; CLARITY &amp; EXPERTISE</span><span class="page">7</span></div>
  </section>

  <section class="slide section" style="left:800px;top:683px">
    <div class="white-rule" style="top:139px"></div>
    <div class="thanks">Thank you</div>
  </section>

  <div class="caption" style="left:412px;top:902px">Interior Slides</div>
  <div class="caption" style="left:976px;top:902px">Section Slide</div>
</body>
</html>
```